Luxury Business Card Design for Velvet Coach

I need a high-end, luxury business card design for my premium limo service, Velvet Coach. The card should reflect elegance and exclusivity, using a black and gold color scheme with a minimalist and sophisticated layout. The design should include:

Target Market(s)

High-end clients, corporate executives, luxury travelers, VIPs, and celebrities looking for premium limousine and chauffeur services

Industry/Entity Type

Limo

Contact Information for Business Card

Cluttered design—should be sleek & minimal

Font styles to use
Other font styles liked:
• CINZEL DECORATIVE

Requirements
Must have
• 📞 416-383-RIDE (416-383-7433) 📞 Toll-Free: 1 (888) 294-RIDE (7433) Email: book@velvet-coach.com
Nice to have
• QR Code , I need a high-end, luxury business card design for my premium limo service, Velvet Coach. The card should reflect elegance and exclusivity, using a black and gold color scheme with a minimalist and sophisticated layout. It should align with the branding, luxury feel, and premium aesthetics seen on our website www.velvet-coach.com.

```html
<!DOCTYPE html>
<html lang="en">
<head>
<meta charset="utf-8">
<title>Velvet Coach — Business Card</title>
<link rel="stylesheet" href="https://fonts.googleapis.com/css2?family=Cinzel:wght@400;600;700&display=swap">
<style>
  :root {
    --page: #1d1d21;
    --card: #0c0c0d;
    --card-edge: #15151a;
    --gold: #c9a24a;
    --gold-light: #e6c877;
    --ink-light: #e9e6df;
    --emboss: #141416;
  }
  * { box-sizing: border-box; margin: 0; padding: 0; }
  html, body { width: 1200px; height: 947px; overflow: hidden; }
  body {
    background: var(--page);
    font-family: "Cinzel", serif;
    display: flex;
    flex-direction: column;
    align-items: center;
    justify-content: space-evenly;
  }
  .card {
    position: relative;
    width: 760px;
    height: 434px;
    background: var(--card);
    border-bottom: 3px solid var(--gold);
    border-right: 3px solid var(--gold);
    overflow: hidden;
  }

  /* Front */
  .card--front {
    display: flex;
    flex-direction: column;
    align-items: center;
    justify-content: center;
    gap: 14px;
  }
  .brand-mark {
    width: 74px; height: 74px;
    border-radius: 50%;
    border: 2px solid var(--gold);
  }
  .brand-name {
    font-weight: 700;
    font-size: 64px;
    letter-spacing: 2px;
    color: var(--gold);
    line-height: 1;
  }
  .brand-tagline {
    font-size: 15px;
    letter-spacing: 9px;
    color: var(--ink-light);
    text-transform: uppercase;
  }

  /* Back */
  .card--back { padding: 44px 52px; }
  .back-brand { display: flex; flex-direction: column; gap: 6px; }
  .back-brand .brand-name { font-size: 34px; }
  .back-brand .brand-tagline { font-size: 8px; letter-spacing: 5px; }
  .holder { margin-top: 34px; }
  .holder-name {
    font-weight: 700;
    font-size: 34px;
    color: var(--gold);
    letter-spacing: 1px;
    line-height: 1;
  }
  .holder-title {
    margin-top: 6px;
    font-size: 17px;
    color: var(--ink-light);
    letter-spacing: 1px;
  }
  .contacts { margin-top: 30px; list-style: none; display: flex; flex-direction: column; gap: 8px; }
  .contact {
    display: flex; align-items: center; gap: 14px;
    font-size: 16px; color: var(--ink-light); letter-spacing: 0.5px;
  }
  .contact svg { width: 15px; height: 15px; fill: none; stroke: var(--gold); stroke-width: 2; flex: none; }
  .contact .solid { fill: var(--gold); stroke: none; }
  .emboss-area {
    position: absolute;
    right: -90px; top: 40px;
    width: 420px; height: 420px;
    border-radius: 50%;
    background: radial-gradient(circle at 45% 45%, var(--emboss), var(--card) 70%);
  }
</style>
</head>
<body>
  <section class="card card--front">
    <span class="brand-mark"></span>
    <h1 class="brand-name">VELVET COACH</h1>
    <p class="brand-tagline">Where the class meets velvet</p>
  </section>

  <section class="card card--back">
    <div class="emboss-area" role="img" aria-label="Blind-embossed brand decoration"></div>
    <div class="back-brand">
      <h2 class="brand-name">VELVET COACH</h2>
      <p class="brand-tagline">Where the class meets velvet</p>
    </div>
    <div class="holder">
      <p class="holder-name">MARCUS HALE</p>
      <p class="holder-title">CEO &amp; FOUNDER</p>
    </div>
    <ul class="contacts">
      <li class="contact">
        <svg viewBox="0 0 16 16"><path class="solid" d="M3 1.5l3 3-1.6 1.8c.9 2 2.4 3.5 4.3 4.3L10.5 9l3 3-2 2.5C6 14 2 10 1.5 4.5z"/></svg>
        416-383-RIDE (416-383-7433)
      </li>
      <li class="contact">
        <svg viewBox="0 0 16 16"><path class="solid" d="M3 1.5l3 3-1.6 1.8c.9 2 2.4 3.5 4.3 4.3L10.5 9l3 3-2 2.5C6 14 2 10 1.5 4.5z"/></svg>
        1 (888) 294-RIDE (7433)
      </li>
      <li class="contact">
        <svg viewBox="0 0 16 16"><rect x="1.5" y="3.5" width="13" height="9"/><path d="M1.5 3.5L8 9l6.5-5.5"/></svg>
        BOOK@VELVET-COACH.COM
      </li>
      <li class="contact">
        <svg viewBox="0 0 16 16"><circle cx="8" cy="8" r="6.5"/><ellipse cx="8" cy="8" rx="2.8" ry="6.5"/><path d="M1.5 8h13"/></svg>
        WWW.VELVET-COACH.COM
      </li>
    </ul>
  </section>
</body>
</html>
```